Morvena Aesthetics Skin Care Flyer

8 1/2" x 11" three-folded brochure that will have a front panel which will show our Morvena Aesthetics logo and state that this is a Facial Menu. It might have our phone number on it and "call for appointment". The left inside flap will provide information about what we do and about the importance of facials and the rest will list services and pricing.

Kestwick Salon & Spa will not have a logo featured but it is important to show their address. Morvena Aesthetics has a newly designed logo but I am not sure how to upload it at this time. I do have a Vector file of our logo and hope to figure out the best way to make it available to all.Thank you. Added Sunday, April 26, 2015

```html
<!DOCTYPE html>
<html lang="en">
<head>
<meta charset="utf-8">
<title>Morvena Aesthetics – Facial Menu</title>
<link href="https://fonts.googleapis.com/css2?family=Didact+Gothic&family=Montserrat:wght@600;700&display=swap" rel="stylesheet">
<style>
  :root {
    --paper: #ffffff;
    --ink: #2a2a2a;
    --ink-strong: #111111;
    --gold: #c9a23a;
    --gold-soft: #e2c46e;
    --skin-light: #f3e3d8;
    --skin-mid: #e8cfc0;
    --oil-green: #b9c77a;
    --oil-gold: #e6c766;
  }
  * { margin: 0; padding: 0; box-sizing: border-box; }
  html, body { width: 1200px; height: 927px; overflow: hidden; background: var(--paper); }
  body { font-family: "Didact Gothic", "Century Gothic", sans-serif; color: var(--ink); }
  .brochure { position: relative; width: 1200px; height: 927px; background: var(--paper); }

  /* Inside flap */
  .initial-mark {
    position: absolute; left: 18px; top: 14px; width: 244px; height: 108px;
    background: linear-gradient(135deg, var(--gold-soft), var(--gold) 55%, rgba(201,162,58,0.15) 100%);
  }
  .intro { position: absolute; left: 72px; top: 132px; width: 262px; font-size: 16.5px; line-height: 25.5px; }
  .intro p { margin-bottom: 25.5px; }
  .intro p.lead { text-indent: 15px; margin-bottom: 0; }

  .brand { position: absolute; left: 78px; top: 676px; width: 290px; text-align: center; }
  .brand-name { font-size: 31px; color: var(--gold); letter-spacing: 0.5px; }
  .address { position: absolute; left: 78px; top: 762px; width: 290px; text-align: center; font-size: 15.5px; line-height: 22px; color: var(--ink-strong); font-style: normal; }
  .appointments { position: absolute; left: 78px; top: 818px; width: 290px; text-align: center; font-family: "Montserrat", sans-serif; font-weight: 600; font-size: 18px; color: var(--ink-strong); }

  /* Service columns */
  .column { position: absolute; font-size: 15px; line-height: 18.5px; }
  .column-middle { left: 446px; top: 50px; width: 298px; }
  .column-right { left: 802px; top: 104px; width: 345px; }
  .section-title { font-family: "Montserrat", sans-serif; font-weight: 700; font-size: 23px; color: var(--ink-strong); line-height: 26px; }
  .section-sub { font-size: 13px; line-height: 15px; margin-bottom: 14px; }
  .photo-facial { width: 294px; height: 166px; background: linear-gradient(120deg, var(--skin-light), var(--skin-mid) 55%, #f7f1ec); margin-bottom: 30px; }
  .photo-aroma { position: absolute; left: 802px; top: 520px; width: 316px; height: 252px; background: linear-gradient(180deg, #ffffff 0%, var(--oil-gold) 55%, var(--oil-green) 100%); }
  .service { margin-bottom: 18px; }
  .service-name { font-family: "Montserrat", sans-serif; font-weight: 600; font-size: 14px; color: var(--ink-strong); }
  .service-name em { font-style: italic; }
  .products { position: absolute; left: 802px; top: 782px; width: 345px; font-size: 15px; line-height: 18.5px; }
  .products-title { font-family: "Montserrat", sans-serif; font-weight: 700; font-size: 23px; color: var(--ink-strong); line-height: 26px; }
</style>
</head>
<body>
<main class="brochure">

  <section class="flap-intro">
    <div class="initial-mark" role="img" aria-label="Gold brush-lettered initial letter decoration"></div>
    <div class="intro">
      <p class="lead">No matter your skin type; dry, oily, sensitive or any kind of combination, Morvena Aesthetics has a deep cleansing facial that is designed to meet your personal needs.</p>
      <p>Your facial appointment begins with a FREE consultation so that we can initially evaluate your skin if you are a first-time client, or your progress should you already be an existing one.</p>
      <p>Our goal is for you to revel in the joy of a wonderfully healthy glow due to radiant and luminous skin as the result of an incredible treatment that will culminate in an exceptionally relaxing neck and shoulder massage.</p>
    </div>
    <div class="brand">
      <div class="brand-name">Morvena Aesthetics</div>
    </div>
    <address class="address">Kestwick Salon &amp; Spa, Port Halden,<br>NY 11790</address>
    <div class="appointments">Appointments: 631-555-0142</div>
  </section>

  <section class="column column-middle">
    <h2 class="section-title">FACIALS</h2>
    <div class="section-sub">60 Minutes</div>
    <div class="photo-facial" role="img" aria-label="Photo of a woman relaxing during a facial treatment, with a script 'facials' caption"></div>

    <div class="service">
      <div><span class="service-name">Classic European</span>: $70.00</div>
      This revitalizing treatment begins with a deep cleansing, followed by gentle exfoliation to reveal smooth, glowing skin. A revitalizing masque, followed by a nutrient rich moisturizer, will hydrate, protect and help restore the natural balance of your skin.
    </div>
    <div class="service">
      <div><span class="service-name">Anti-Aging</span>: $80.00,</div>
      <div><span class="service-name"><em>add a Glycolic Peel</em></span>: $100</div>
      A highly effective treatment for targeting visible signs of aging (fine lines, wrinkles, sun damage, etc.) and restoring a more youthful appearance. We utilize Vitamin C along with a peptide smoothing serum to produce desirable results. Add a glycolic peel for an even more efficient removal of dead skin layers while stimulating collagen production.
    </div>
    <div class="service">
      <div><span class="service-name">Aroma Therapy</span> :$80.00</div>
      A deep cleansing and exfoliation will restore your skin's natural radiance. The pressure point massage will stimulate blood circulation and revitalize the tissues while the wonderfully fragrant and essential oils soothe your senses and rejuvenate your skin.
    </div>
  </section>

  <section class="column column-right">
    <div><span class="service-name">Acne Glycolic Exfoliation Treatment</span>:</div>
    <div>$95.00</div>
    Acne facials or deep cleansing facials are recommended for clients prone to oily or acneic skin or for those with uneven complexions. We incorporate a combination of thorough steaming, deep cleansing, facial extractions to remove pore-clogging sebum, and a healing mask and moisturizer. Salicylic and glycolic acids are aimed at managing and thwarting acne flare-ups.
    <div>Sensitive Facial...$80.00</div>
    For sensitive skin, this facial utilizes gentle procedures and hypoallergenic products that are appropriate for irritation-prone skin. Those with skin sensitivities should not fear the calming effects of this delicate treatment. Facials for sensitive skin can improve complexion, reduce inflammation and boost your skin's immunity, which will help prevent future irritations.
  </section>

  <div class="photo-aroma" role="img" aria-label="Photo of essential oil bottles, soap, orchid and incense on a leaf, with a script 'Aroma Therapy' caption"></div>

  <section class="products">
    <h2 class="products-title">PRODUCTS</h2>
    <p>We also offer exceptional retail products that allow for further improvement between facials, when at home.</p>
  </section>

</main>
</body>
</html>
```